Dental Design, very professional and noticable

Copperleaf Ridge Dental Surgery is based in Pelican Waters. We are a fast growing dental surgery and are looking for some professional business cards to send to patients.
We would like to see a design that is Vertical and uses the colours Soft Blue, Silver, White and Black. Maybe a full blue side with moto and details on back? Any other ideas or colours that you may think will make the card look unique is fine.
We need all details on the card that are listed above

Target Market(s)

Families, Retired, Other Professionals and Businesses

Industry/Entity Type

Dental

Contact Information for Business Card

Copperleaf Ridge Dental Surgery
Family, Cosmetic, Preventative
Dr. Owen Farrish
Dental Surgeon
BDS (Adel) FAE FADI FICD FPFA
phone: (07)54810296
fax: (07)54926170
email: copperleafridgedental@quillpost.net
http://copperleafridgedental.quillpost.net/

Logo Text

Logo styles of interest
Abstract Logo
Requirements
Must have
• Vertical, Vibrant but Professional, Rounded Edges, Logo on front and back of card (different colours on each side)
Nice to have
• One side completely blue (not sure what shade) with logo and moto on bottom
Other side white, with blue or different coloured logo with details in black and silver?
Logo should show half circle with 1 end as arrow symbolizing pelican waters canal also a magnifine glass also half circled with 1 end as arrow. Any other ideas are welcome.
Should not have
• A tooth. A smile. Toothbrush or Toothpaste. Cornered edges.

```html
<!DOCTYPE html>
<html lang="en">
<head>
<meta charset="utf-8">
<title>Copperleaf Ridge Dental Surgery – Business Card</title>
<link href="https://fonts.googleapis.com/css2?family=Marcellus&family=Open+Sans:wght@400;700;800&family=Arimo:wght@400&display=swap" rel="stylesheet">
<style>
  :root{
    --stage:#262626;
    --paper:#ffffff;
    --navy:#2a3377;
    --gold:#8e742f;
    --ink:#111111;
    --grey:#333333;
  }
  *{box-sizing:border-box;margin:0;padding:0}
  html,body{width:1200px;height:1200px;overflow:hidden;background:var(--stage)}
  .stage{position:relative;width:1200px;height:1200px;display:flex;align-items:center;justify-content:center;gap:70px}
  .card{position:relative;width:420px;height:690px;border-radius:28px;overflow:hidden;box-shadow:0 14px 30px rgba(0,0,0,.45)}

  /* front */
  .card--front{background:var(--paper)}
  .brand{position:absolute;left:30px;right:30px;top:60px;text-align:center}
  .brand__dot{display:block;width:70px;height:70px;border-radius:50%;background:var(--gold);margin:0 auto 18px}
  .brand__name{font-family:"Marcellus",serif;font-size:27px;line-height:1.2;color:var(--gold)}
  .brand__motto{font-family:"Marcellus",serif;font-size:19px;color:var(--gold);margin-top:10px}
  .details{position:absolute;left:38px;right:30px;top:320px}
  .details__name{font-family:"Open Sans",sans-serif;font-weight:800;font-size:32px;line-height:1.2;color:var(--navy);letter-spacing:-.3px}
  .details__title{font-family:"Open Sans",sans-serif;font-weight:700;font-size:11px;color:var(--grey);margin-top:4px}
  .contact{list-style:none;margin-top:24px;font-family:"Arimo",sans-serif;font-size:15.5px;color:var(--ink);line-height:1.7}
  .contact__label{color:var(--navy)}
  .band{position:absolute;left:0;right:0;bottom:0;height:78px}
  .band__gold{position:absolute;left:0;right:0;top:0;height:40px;background:var(--gold)}
  .band__navy{position:absolute;left:0;right:0;bottom:0;height:34px;background:var(--navy)}

  /* back */
  .card--back{background:var(--navy);display:flex;flex-direction:column;align-items:center;justify-content:center;text-align:center;padding:0 36px}
  .card--back .brand__dot{background:var(--paper);width:96px;height:96px;margin-bottom:26px}
  .back__name{font-family:"Marcellus",serif;font-size:33px;line-height:1.22;color:var(--paper)}
  .back__motto{font-family:"Marcellus",serif;font-size:22px;color:var(--paper);margin-top:14px}
</style>
</head>
<body>
<main class="stage">
  <section class="card card--front" aria-label="Card front">
    <div class="brand">
      <span class="brand__dot"></span>
      <p class="brand__name">Copperleaf Ridge<br>Dental Surgery</p>
      <p class="brand__motto">Family, Cosmetic, Preventive</p>
    </div>
    <div class="details">
      <h1 class="details__name">Dr. Owen Farrish</h1>
      <p class="details__title">Dental Surgeon BDS (Adel) FAE FADI FICD FPFA</p>
      <ul class="contact">
        <li><span class="contact__label">Phone:</span> (07)54810296</li>
        <li><span class="contact__label">Fax:</span> (07)54926170</li>
        <li>copperleafridgedental@quillpost.net</li>
        <li>www.copperleafridgedental.quillpost.net</li>
      </ul>
    </div>
    <div class="band"><div class="band__gold"></div><div class="band__navy"></div></div>
  </section>
  <section class="card card--back" aria-label="Card back">
    <span class="brand__dot"></span>
    <p class="back__name">Copperleaf Ridge<br>Dental Surgery</p>
    <p class="back__motto">Family, Cosmetic, Preventive</p>
  </section>
</main>
</body>
</html>
```